Velmora Partners - website for real estate investment company

Create a bold, modern website that reflects Velmora’s success, professionalism, and credibility.
The design must stand out while maintaining a polished, corporate tone. (bold, but understated)
The client just created a new logo, and the website design must be in sync with the logo design. Information about the logo colors, fonts, and message are in the attached design brief.
Updates

Target Market(s)

b2b: banks, brokers, institutional partners, vendors, and property sellers.

Industry/Entity Type

real estate investment company

Number of Pages Required

1 page

Font styles to use
Sans Serif

Colors

Designer to choose colors to be used in the design.

Requirements
Must have
• 1. homepage design (psd) 2. a top banner image (psd) for a default inner page
Nice to have
• please see attached design brief
Should not have

```html
<!DOCTYPE html>
<html lang="en">
<head>
<meta charset="utf-8">
<title>Velmora Partners</title>
<link rel="stylesheet" href="https://fonts.googleapis.com/css2?family=Barlow:wght@600;700&family=Poppins:wght@300;400;500;600;700&display=swap">
<style>
:root{
  --red:#e0202b;
  --red-dark:#c41822;
  --ink:#1d1d1f;
  --grey:#5a5a5a;
  --muted:#8a8a8a;
  --frame:#c8c8c8;
  --page:#ffffff;
  --field:#f1f1f1;
  --footer:#555555;
  --sky-top:#3f7fd0;
  --sky-low:#dfeaf6;
}
*{box-sizing:border-box;margin:0;padding:0}
html,body{width:1200px;height:4799px;overflow:hidden}
body{background:var(--frame);font-family:'Poppins',sans-serif;color:var(--ink);position:relative}
.page{position:absolute;left:60px;top:47px;width:1069px;height:4700px;background:var(--page);overflow:hidden}
.abs{position:absolute}
.btn{position:absolute;background:var(--red);color:#fff;font-weight:600;font-size:12px;border-radius:4px;display:flex;align-items:center;justify-content:center;box-shadow:0 2px 4px rgba(0,0,0,.25)}
.section-title{position:absolute;left:0;width:1069px;text-align:center;font-size:32px;font-weight:400;letter-spacing:1px;color:#2b2b2b}
.ph{position:absolute}

/* hero */
.hero-sky{left:0;top:0;width:1069px;height:717px;background:linear-gradient(180deg,var(--sky-top) 0%,#8db4e4 40%,var(--sky-low) 75%,#fff 100%)}
.hero-card{left:87px;top:29px;width:894px;height:620px;border-radius:12px;background:linear-gradient(180deg,#fff 0%,#fff 60%,rgba(255,255,255,.2) 100%)}
.logo{font-family:'Poppins',sans-serif;font-weight:700;color:var(--ink);letter-spacing:0}
.nav{position:absolute;left:312px;top:52px;display:flex;gap:24px;font-size:11px;color:#222}
.hero-title{position:absolute;left:0;width:1069px;text-align:center;font-family:'Barlow',sans-serif;font-weight:700;line-height:1}
.hero-house{left:80px;top:300px;width:910px;height:390px;border-radius:6px;background:linear-gradient(180deg,#d9dee4 0%,#b7c0ca 50%,#8e9aa6 100%)}
.intro{left:136px;top:456px;width:292px;height:97px;background:rgba(110,110,110,.75);color:#f2f2f2;font-size:9.5px;line-height:1.5;padding:8px 20px;border-radius:3px}
.search{left:186px;top:603px;width:695px;height:108px;background:var(--red);border-radius:6px}
.search h3{position:absolute;left:24px;top:10px;color:#fff;font-size:18px;font-weight:600}
.field{position:absolute;top:45px;width:165px;height:48px;background:#fff;border-radius:4px;padding:7px 8px}
.field b{display:flex;align-items:center;gap:5px;font-size:11px;font-weight:500}
.field span{display:block;font-size:8px;color:#444;margin-top:4px}
.search .go{position:absolute;left:570px;top:49px;width:104px;height:37px;background:#111;color:#fff;font-size:11px;font-weight:600;border-radius:4px;display:flex;align-items:center;justify-content:center}

/* about */
.about h2{position:absolute;left:134px;top:790px;font-size:32px;font-weight:400;letter-spacing:1px}
.about .lead{position:absolute;left:149px;top:853px;width:352px;font-size:11.5px;line-height:1.45;color:#333;border-left:3px solid var(--red);padding-left:14px}
.about .point{position:absolute;left:160px;width:340px;font-size:11.5px;line-height:1.45;color:#333}
.about .point::before{content:"";position:absolute;left:-10px;top:7px;width:4px;height:4px;background:#555;border-radius:50%}
.stat{position:absolute;top:1086px;width:120px}
.stat strong{display:block;color:var(--red);font-size:24px;font-weight:600}
.stat small{display:block;font-size:9px;line-height:1.4;color:#333}
.stat.div{border-left:2px solid var(--red);padding-left:14px;height:66px}
.about-shadow{left:561px;top:806px;width:385px;height:398px;background:var(--red);border-radius:8px}
.about-photo{left:551px;top:801px;width:384px;height:393px;border-radius:8px;background:linear-gradient(135deg,#cfd6de 0%,#9ea9b5 40%,#e8e2d6 70%,#c5b6a0 100%)}

/* strategy */
.step{position:absolute;width:56px;height:56px;border-radius:50%;border:1.5px solid #b9b9b9;display:flex;align-items:center;justify-content:center;font-size:22px;color:#555;background:#fff}
.step.active{background:var(--red);color:#fff;border:none;box-shadow:0 0 0 5px #fff,0 0 0 6px #f2a5a9}
.step.first{border-color:#f2a5a9}
.track{position:absolute;top:1384px;height:1px;background:#ddd}
.arrow{position:absolute;width:34px;height:34px;border-radius:50%;border:1.5px solid #999;display:flex;align-items:center;justify-content:center;background:#fff}
.strategy-photo{left:313px;top:1456px;width:441px;height:341px;border-radius:14px;background:linear-gradient(180deg,#b9c6d2 0%,#9aa39c 50%,#5e9a40 100%)}

/* sets apart */
.feature{position:absolute;top:2011px;width:180px;text-align:center}
.feature .ic{width:62px;height:62px;margin:0 auto 10px;border-radius:50%;border:3px solid #444;display:flex;align-items:center;justify-content:center}
.feature.hot .ic{border-color:var(--red)}
.feature p{font-size:15px;line-height:1.15;color:#333}
.apart-house{left:80px;top:2150px;width:910px;height:420px;border-radius:6px;background:linear-gradient(180deg,#e4e9ef 0%,#c3ccd5 55%,#b39a80 100%)}

/* portfolio */
.card{position:absolute;width:190px;text-align:center}
.card .img{width:190px;border-radius:3px}
.card h4{font-size:15px;font-weight:400;margin-top:22px;color:#333}
.card p{font-size:8px;line-height:1.7;color:#777;margin-top:6px}
.card a{display:block;font-size:11px;font-weight:600;margin-top:10px;color:#222;text-decoration:none}

/* testimonials */
.avatar{left:473px;top:3292px;width:122px;height:122px;border-radius:50%;background:radial-gradient(circle,#f6d3d8 0%,#eab4bc 100%)}
.handle{left:0;width:1069px;text-align:center;font-size:10px;color:#999}
.quote{left:250px;width:570px;top:3501px;text-align:center;font-size:9px;line-height:1.75;color:#555}

/* contact */
.connect{left:152px;top:3690px;width:397px;height:492px;border-radius:14px;background:#fff;box-shadow:0 0 0 4px #eee,0 6px 12px rgba(0,0,0,.08)}
.connect h2{position:absolute;left:37px;top:74px;font-size:27px;font-weight:500;letter-spacing:1.5px;color:#333}
.connect .sub{position:absolute;left:37px;top:126px;width:290px;font-size:9px;line-height:1.6;color:#555}
.input{position:absolute;left:36px;width:324px;background:var(--field);font-size:11px;padding:8px 14px;color:#333}
.submit{left:36px;top:421px;width:324px;height:36px;border-radius:4px;box-shadow:none}
.location h2{position:absolute;left:583px;top:3704px;font-size:26px;font-weight:500;letter-spacing:1px;color:#333}
.location .sub{position:absolute;left:583px;top:3746px;width:290px;font-size:9px;line-height:1.6;color:#555}
.map{left:581px;top:3804px;width:333px;height:305px;border-radius:6px;background:linear-gradient(135deg,#ededed 0%,#dcdcdc 50%,#f2e2b6 100%)}
.social-dot{position:absolute;top:4155px;width:24px;height:24px;border-radius:50%;border:1px solid #f0c2c5;background:#fff;display:flex;align-items:center;justify-content:center}
.social-dot i{width:10px;height:10px;border-radius:50%;background:var(--red)}

/* footer */
.footer{left:0;top:4256px;width:1069px;height:407px;background:var(--footer);color:#fff}
.footer .logo{position:absolute;left:132px;top:100px;font-size:56px;color:#fff}
.footer .about-text{position:absolute;left:133px;top:188px;width:330px;font-size:9.5px;line-height:1.9}
.footer h5{position:absolute;top:106px;font-size:17px;font-weight:600}
.footer ul{position:absolute;list-style:none;font-size:10.5px}
.links li{height:34px}
.follow li{height:27px;display:flex;align-items:center;gap:10px}
.follow li::before{content:"";width:18px;height:18px;border-radius:50%;background:#fff;box-shadow:inset 0 0 0 5px #fff,inset 0 0 0 9px var(--red)}
.copyright{left:0;top:4673px;width:1069px;text-align:center;font-size:10.5px;color:#222}
</style>
</head>
<body>
<div class="page">

  <!-- hero -->
  <div class="ph hero-sky" role="img" aria-label="Blue sky with soft white clouds"></div>
  <div class="abs hero-card"></div>
  <div class="abs logo" style="left:132px;top:44px;font-size:30px;">VELMORA</div>
  <nav class="nav"><span>Home</span><span>Our Story</span><span>Investment Strategy</span><span>What Sets Us Apart</span><span>Our Portfolio</span></nav>
  <div class="btn" style="left:838px;top:44px;width:97px;height:34px;">Contact</div>
  <div class="ph hero-house" role="img" aria-label="Modern two-storey luxury house with glass balcony on a lawn"></div>
  <div class="hero-title" style="top:130px;font-size:76px;color:var(--red);">Your Partner</div>
  <div class="hero-title" style="top:203px;font-size:76px;color:var(--ink);">In Luxury Glamping</div>
  <div class="abs intro">Velmora Partners Is A Vertically Integrated Real Estate Investment Firm With A Proven Four-Decade Track Record. We Acquire, Reposition, And Operate High-Performing Assets Across Multiple Sectors — Always With A Focus On Exceptional, Risk-Adjusted Returns.</div>
  <div class="btn" style="left:836px;top:538px;width:97px;height:30px;">Learn More</div>

  <div class="abs search">
    <h3>Buy Sell</h3>
    <div class="field" style="left:24px;">
      <b><svg width="11" height="13" viewBox="0 0 12 14"><path d="M6 0C2.7 0 0 2.6 0 5.8 0 10 6 14 6 14s6-4 6-8.2C12 2.6 9.3 0 6 0zm0 8a2.3 2.3 0 1 1 0-4.6A2.3 2.3 0 0 1 6 8z" fill="#111"/></svg>LOCATION</b>
      <span>Enim Ad Minim Veniam</span>
    </div>
    <div class="field" style="left:201px;">
      <b><svg width="14" height="12" viewBox="0 0 14 12"><path d="M7 0 0 6h2v6h4V8h2v4h4V6h2z" fill="#111"/></svg>TYPE OF HOUSE</b>
      <span>Enim Ad Minim Veniam</span>
    </div>
    <div class="field" style="left:378px;">
      <b><svg width="11" height="13" viewBox="0 0 11 13"><rect x="3" y="0" width="5" height="3" fill="#111"/><path d="M2 4h7l2 9H0z" fill="#111"/></svg>BUDGET</b>
      <span>Enim Ad Minim Veniam</span>
    </div>
    <div class="go">Search Now</div>
  </div>

  <!-- about -->
  <section class="about">
    <h2>ABOUT US</h2>
    <p class="lead">From The Beginning, Hometide Has Been Transforming Home Improvement With Innovative, Sustainable Solutions. We've Made It Easier For Everyone To Access The Tools They Need To Create Energy-Efficient, Resilient Homes That Stand The Test Of Time.</p>
    <p class="point" style="top:960px;">Fast Approvals &amp; Closings Get Approved Within 24 Hours And Close In As Little As 7–10 Days</p>
    <p class="point" style="top:1016px;">Flexible Loan Terms Designed To Meet Your Deal's Timeline And Goals.</p>
    <div class="stat" style="left:133px;"><strong>23,000+</strong><small>Multifamily &amp;<br>Healthcare Units</small></div>
    <div class="stat div" style="left:252px;"><strong>$300+</strong><small>Million Invested In<br>Renovations</small></div>
    <div class="stat div" style="left:387px;"><strong>15K+</strong><small>Lorem Ipsum Dolor Sit<br>Amet Consectetur.</small></div>
    <div class="btn" style="left:132px;top:1171px;width:106px;height:34px;">Learn More</div>
    <div class="abs about-shadow"></div>
    <div class="ph about-photo" role="img" aria-label="Three colleagues at a desk with a laptop and small wooden house models"></div>
  </section>

  <!-- investment strategy -->
  <h2 class="section-title" style="top:1278px;">INVESTMENT STRATEGY</h2>
  <div class="track" style="left:251px;width:570px;"></div>
  <div class="step first" style="left:195px;top:1356px;">01</div>
  <div class="step active" style="left:421px;top:1356px;">02</div>
  <div class="step" style="left:616px;top:1356px;">03</div>
  <div class="step" style="left:812px;top:1356px;">04</div>
  <div class="arrow" style="left:229px;top:1609px;border-color:var(--red);"><svg width="8" height="8" viewBox="0 0 8 8"><path d="M6 0 1 4l5 4z" fill="var(--red)"/></svg></div>
  <div class="arrow" style="left:804px;top:1609px;"><svg width="8" height="8" viewBox="0 0 8 8"><path d="M2 0l5 4-5 4z" fill="#333"/></svg></div>
  <div class="ph strategy-photo" role="img" aria-label="Family standing on a lawn in front of a suburban house"></div>
  <div class="btn" style="left:443px;top:1833px;width:183px;height:31px;">Schedule a Consultation</div>

  <!-- what sets us apart -->
  <h2 class="section-title" style="top:1938px;">WHAT SETS US APART</h2>
  <div class="feature" style="left:124px;"><div class="ic"><svg width="30" height="24" viewBox="0 0 30 24"><circle cx="15" cy="6" r="4" fill="#444"/><circle cx="6" cy="9" r="3" fill="#444"/><circle cx="24" cy="9" r="3" fill="#444"/><path d="M8 22c0-5 3-8 7-8s7 3 7 8zM0 22c0-4 2-7 6-7 1 0 2 .3 3 .8C7 17 6 19 6 22zM30 22c0-4-2-7-6-7-1 0-2 .3-3 .8 2 1.2 3 3.2 3 6.2z" fill="#444"/></svg></div><p>Experience&amp; Track<br>Record</p></div>
  <div class="feature" style="left:338px;"><div class="ic"><svg width="24" height="28" viewBox="0 0 24 28"><circle cx="12" cy="5" r="4" fill="#444"/><rect x="9" y="11" width="6" height="16" fill="#444"/><circle cx="3" cy="14" r="2.5" fill="#444"/><circle cx="21" cy="14" r="2.5" fill="#444"/></svg></div><p>Tailored Insurance<br>Solutions</p></div>
  <div class="feature hot" style="left:550px;"><div class="ic"><svg width="30" height="26" viewBox="0 0 30 26"><circle cx="15" cy="8" r="4" fill="var(--red)"/><path d="M8 20c0-4 3-7 7-7s7 3 7 7z" fill="var(--red)"/><circle cx="4" cy="4" r="2" fill="var(--red)"/><circle cx="26" cy="4" r="2" fill="var(--red)"/><circle cx="4" cy="20" r="2" fill="var(--red)"/><circle cx="26" cy="20" r="2" fill="var(--red)"/></svg></div><p>End-To-End Policy<br>Management</p></div>
  <div class="feature" style="left:763px;"><div class="ic"><svg width="28" height="26" viewBox="0 0 28 26"><rect x="4" y="6" width="20" height="14" rx="2" fill="none" stroke="#444" stroke-width="2.5"/><circle cx="14" cy="13" r="3" fill="var(--red)"/><rect x="11" y="0" width="6" height="4" fill="#444"/><rect x="9" y="22" width="10" height="3" fill="#444"/></svg></div><p>Strong Customer<br>Service</p></div>
  <div class="ph apart-house" role="img" aria-label="Modern white villa with wood panelling and glass walls on a reflective deck"></div>

  <!-- portfolio -->
  <h2 class="section-title" style="top:2662px;">OUR PORTFOLIO</h2>
  <div class="card" style="left:134px;top:2738px;">
    <div class="img" role="img" aria-label="Two-storey house with a porch under blue sky" style="height:196px;background:linear-gradient(180deg,#8fb3de 0%,#a99c8e 55%,#6a9a4c 100%);"></div>
    <h4>Visual Presentation</h4><p>Lorem Ipsum Dolor Sit Amet<br>Consectetur. Quis</p><a>LEARN MORE</a>
  </div>
  <div class="card" style="left:337px;top:2738px;">
    <div class="img" role="img" aria-label="Stone-fronted family house with green lawn" style="height:304px;background:linear-gradient(180deg,#93b4dc 0%,#9a9a96 55%,#5e9444 100%);"></div>
    <h4>Featured Properties</h4><p>Lorem Ipsum Dolor Sit Amet<br>Consectetur. Quis</p><a>LEARN MORE</a>
  </div>
  <div class="card" style="left:542px;top:2738px;">
    <div class="img" role="img" aria-label="Modern blue glass apartment tower" style="height:304px;background:linear-gradient(180deg,#3f7bcc 0%,#7aa6da 60%,#4a5a6a 100%);"></div>
    <h4>Property Categories</h4><p>Lorem Ipsum Dolor Sit Amet<br>Consectetur. Quis</p><a>LEARN MORE</a>
  </div>
  <div class="card" style="left:745px;top:2738px;">
    <div class="img" role="img" aria-label="Cream house with gabled roof and front garden" style="height:196px;background:linear-gradient(180deg,#93b8e0 0%,#cbc6ad 55%,#5e9a44 100%);"></div>
    <h4>Portfolio Overview</h4><p>Lorem Ipsum Dolor Sit Amet<br>Consectetur. Quis</p><a>LEARN MORE</a>
  </div>

  <!-- testimonials -->
  <h2 class="section-title" style="top:3218px;">TESTIMONIALS</h2>
  <div class="ph avatar" role="img" aria-label="Portrait of the client giving the testimonial"></div>
  <div class="abs handle" style="top:3423px;">@marencastell</div>
  <div class="abs" style="left:0;width:1069px;text-align:center;top:3438px;font-size:20px;font-weight:600;">Maren Castell</div>
  <div class="abs handle" style="top:3470px;font-size:9px;color:#333;">445,789 <span style="color:#aaa;">Followers</span></div>
  <div class="arrow" style="left:226px;top:3437px;width:24px;height:24px;background:#555;border:none;"><svg width="8" height="8" viewBox="0 0 8 8"><path d="M6 0 1 4l5 4z" fill="#fff"/></svg></div>
  <div class="arrow" style="left:817px;top:3437px;width:24px;height:24px;background:#555;border:none;"><svg width="8" height="8" viewBox="0 0 8 8"><path d="M2 0l5 4-5 4z" fill="#fff"/></svg></div>
  <p class="abs quote">Empower Your Business With Comprehensive Agency Solutions That Meet Your Goals With A Comprehensive Agency Approach. Empower Your Business With Comprehensive Agency Solutions That Meet Your Goals With A Comprehensive Agency Approach And Lasting Solutions</p>
  <div class="btn" style="left:493px;top:3578px;width:80px;height:30px;">Follow</div>

  <!-- contact -->
  <div class="abs connect">
    <h2>LET'S CONNECT,</h2>
    <p class="sub">Your Satisfaction Is Our Priority. We Work Closely With You To Understand</p>
    <div class="input" style="top:171px;height:30px;">Name</div>
    <div class="input" style="top:222px;height:30px;">Email</div>
    <div class="input" style="top:268px;height:129px;">Message</div>
    <div class="btn submit">sumbit</div>
  </div>
  <div class="location">
    <h2>OUR LOCATION</h2>
    <p class="sub">Our Goal Is Not Just To Achieve Short-Term Gains But To Build Lasting Value.</p>
    <div class="ph map" role="img" aria-label="Street map of the office area with a red location pin"></div>
    <svg class="abs" style="left:727px;top:3855px;" width="42" height="58" viewBox="0 0 42 58"><path d="M21 0C9.4 0 0 9.2 0 20.5 0 36 21 58 21 58s21-22 21-37.5C42 9.2 32.6 0 21 0z" fill="var(--red)"/><circle cx="21" cy="20" r="8" fill="#fff"/></svg>
    <div class="abs" style="left:581px;top:4124px;font-size:12px;color:#333;">Social Media</div>
    <div class="social-dot" style="left:580px;"><i></i></div>
    <div class="social-dot" style="left:615px;"><i></i></div>
    <div class="social-dot" style="left:651px;"><i></i></div>
  </div>

  <!-- footer -->
  <footer class="abs footer">
    <div class="logo">VELMORA</div>
    <p class="about-text">Our Team Of Talented Architects, Designers, And Planners Work Collaboratively To Turn Visionary Concepts Into Reality, Ensuring Each Project Reflects Our Core Values Of Creativity, Sustainability, And Precision.</p>
    <h5 style="left:680px;">Use Links</h5>
    <ul class="links" style="left:685px;top:146px;"><li>Home</li><li>Our Story</li><li>Investment Strategy</li><li>What Sets Us Apart</li><li>Our Portfolio</li></ul>
    <h5 style="left:836px;">Follow Us</h5>
    <ul class="follow" style="left:836px;top:141px;"><li>Friendbook</li><li>Chirper</li><li>Snapgram</li><li>WorkNet</li><li>Portfolia</li></ul>
  </footer>
  <div class="abs copyright">Copyright © 2025 All Rights Reserved.</div>
</div>
</body>
</html>
```